Dorm Svc Mission Statement Graphic

We need an engaging and bold design that highlights our department's new mission statement. It must include our logo and department colors. It should also include the college logo. Dorm Svc logo standards are:
Blue is PMS 301C
Green is PMS 368C
Gray is PMS CGray9
"LVC" font is FF More Wide Black Italic
"Dormitory Services" font is sans serif Officina

College logo is PMS 301C

The text of our mission statement is:
Larkspur Valley College's department of Dormitory Services strives to provide safe living environments, with a community that fosters personal growth and academic success; through a student centered foundation that encourages residents to recognize their potential and diversity.
We aim to build an accessible and sustainable lifestyle in the heart of the Colorado Rockies.

Industry/Entity Type

College

```html
<!DOCTYPE html>
<html lang="en">
<head>
<meta charset="utf-8">
<title>Dormitory Services Mission Statement</title>
<link rel="stylesheet" href="https://fonts.googleapis.com/css2?family=Lobster+Two:wght@700&family=Merriweather:ital,wght@0,700;1,300&display=swap">
<style>
  :root {
    --blue: #2a5f8e;
    --blue-deep: #1f4f7a;
    --green: #5aa83c;
    --green-light: #c4e3ae;
    --paper: #ffffff;
    --stage: #ececec;
  }
  * { margin: 0; padding: 0; box-sizing: border-box; }
  html, body { width: 1200px; height: 745px; overflow: hidden; }
  body { background: var(--stage); position: relative; font-family: "Merriweather", Georgia, serif; }

  .mission-card {
    position: absolute;
    background: var(--paper);
    overflow: hidden;
  }
  .mission-card--landscape { left: 51px; top: 142px; width: 562px; height: 435px; }
  .mission-card--portrait { left: 659px; top: 52px; width: 472px; height: 613px; }

  .card-shapes { position: absolute; inset: 0; width: 100%; height: 100%; }

  .college-mark {
    position: absolute;
    left: 8px;
    top: 10px;
    display: flex;
    align-items: flex-start;
    gap: 5px;
    color: var(--blue);
    font-weight: 700;
    font-size: 9.5px;
    line-height: 1.15;
  }
  .college-mark__square { width: 15px; height: 15px; background: var(--blue); flex: none; margin-top: 2px; }
  .mission-card--portrait .college-mark { font-size: 10.5px; }

  .mission-title {
    position: absolute;
    font-family: "Lobster Two", "Brush Script MT", cursive;
    font-weight: 700;
    color: var(--blue);
    line-height: 1;
  }
  .mission-card--landscape .mission-title { left: 62px; top: 95px; font-size: 42px; }
  .mission-card--portrait .mission-title { right: 27px; top: 148px; font-size: 45px; }

  .mission-text {
    position: absolute;
    font-style: italic;
    font-weight: 300;
    color: var(--blue);
  }
  .mission-card--landscape .mission-text { left: 63px; top: 162px; width: 440px; font-size: 13.6px; line-height: 19.5px; }
  .mission-card--portrait .mission-text { right: 27px; top: 200px; width: 405px; font-size: 15.4px; line-height: 22px; text-align: right; }

  .dept-mark {
    position: absolute;
    right: 18px;
    bottom: 16px;
    display: flex;
    align-items: center;
    gap: 7px;
    color: var(--paper);
    font-weight: 700;
  }
  .dept-mark__circle { width: 16px; height: 16px; border-radius: 50%; background: var(--paper); flex: none; }
  .dept-mark__name { display: flex; flex-direction: column; align-items: flex-end; line-height: 1; }
  .dept-mark__initials { font-size: 38px; letter-spacing: 1px; }
  .dept-mark__dept { font-size: 11px; margin-top: 4px; }
  .mission-card--portrait .dept-mark__initials { font-size: 40px; }
  .mission-card--portrait .dept-mark__dept { font-size: 12px; }
</style>
</head>
<body>

<section class="mission-card mission-card--landscape">
  <svg class="card-shapes" viewBox="0 0 562 435" preserveAspectRatio="none" aria-hidden="true">
    <defs>
      <linearGradient id="leafLandscape" x1="0" y1="0" x2="1" y2="0">
        <stop offset="0" stop-color="#5aa83c"/>
        <stop offset="1" stop-color="#c4e3ae"/>
      </linearGradient>
      <linearGradient id="lakeLandscape" x1="0" y1="0" x2="1" y2="0">
        <stop offset="0" stop-color="#eef1f5"/>
        <stop offset="0.45" stop-color="#8ea6c0"/>
        <stop offset="0.68" stop-color="#2a5f8e"/>
        <stop offset="1" stop-color="#1f4f7a"/>
      </linearGradient>
    </defs>
    <path d="M0 0 H562 V0 C380 6 120 22 0 95 Z" fill="url(#leafLandscape)"/>
    <path d="M0 435 V430 C220 430 380 410 562 230 V435 Z" fill="url(#lakeLandscape)"/>
  </svg>

  <div class="college-mark">
    <span>Larkspur<br>Valley<br>College</span>
    <span class="college-mark__square"></span>
  </div>

  <h1 class="mission-title">Our mission</h1>
  <p class="mission-text">Larkspur Valley College's department of Dormitory Services strives to provide safe living environments, with a community that fosters personal growth and academic success; through a student centered foundation that encourages residents to recognize their potential and diversity.<br>We aim to build an accessible and sustainable lifestyle in the heart of the Colorado Rockies.</p>

  <div class="dept-mark">
    <span class="dept-mark__circle"></span>
    <span class="dept-mark__name">
      <span class="dept-mark__initials">LVC</span>
      <span class="dept-mark__dept">Dormitory Services</span>
    </span>
  </div>
</section>

<section class="mission-card mission-card--portrait">
  <svg class="card-shapes" viewBox="0 0 472 613" preserveAspectRatio="none" aria-hidden="true">
    <defs>
      <linearGradient id="leafPortrait" x1="0" y1="0" x2="1" y2="0">
        <stop offset="0" stop-color="#5aa83c"/>
        <stop offset="1" stop-color="#c4e3ae"/>
      </linearGradient>
      <linearGradient id="lakePortrait" x1="0" y1="0" x2="1" y2="0">
        <stop offset="0" stop-color="#eef1f5"/>
        <stop offset="0.4" stop-color="#8ea6c0"/>
        <stop offset="0.62" stop-color="#2a5f8e"/>
        <stop offset="1" stop-color="#1f4f7a"/>
      </linearGradient>
    </defs>
    <path d="M0 0 H472 V0 C300 6 80 30 0 132 Z" fill="url(#leafPortrait)"/>
    <path d="M0 613 C220 605 400 530 472 330 V613 Z" fill="url(#lakePortrait)"/>
  </svg>

  <div class="college-mark">
    <span>Larkspur<br>Valley<br>College</span>
    <span class="college-mark__square"></span>
  </div>

  <h1 class="mission-title">Our mission</h1>
  <p class="mission-text">Larkspur Valley College's department of Dormitory Services strives to provide safe living environments, with a community that fosters personal growth and academic success; through a student centered foundation that encourages residents to recognize their potential and diversity.<br>We aim to build an accessible and sustainable lifestyle in the heart of the Colorado Rockies.</p>

  <div class="dept-mark">
    <span class="dept-mark__circle"></span>
    <span class="dept-mark__name">
      <span class="dept-mark__initials">LVC</span>
      <span class="dept-mark__dept">Dormitory Services</span>
    </span>
  </div>
</section>

</body>
</html>
```